Gablestone Inspections Business Card

I need a business card for my new company. The company is going to provide home inspections. The name of the company is Gablestone Inspections. I am not sure if I want a single sided card or a double. I have a logo already that I want to incorporate into the card design. I was wondering if I should incorporate a catch phrase on my card or not. If I did the phrase would be "The Intelligent Choice for Home Inspections" but i am unsure how or if to use it on a card. The following information needs to be on the card.
Home Inspection
My Name: Tobias R. Fenwick Phone Number: 555-317-6420 Email: tfenwick@gablestoneinspections.com Website: www.gablestoneinspections.com NY HI License # 27300592415

```html
<!DOCTYPE html>
<html lang="en">
<head>
<meta charset="utf-8">
<title>Gablestone Inspections Business Card</title>
<link href="https://fonts.googleapis.com/css2?family=Questrial&display=swap" rel="stylesheet">
<style>
  :root {
    --stage: #3a3a3c;
    --card-dark: #1e1a1f;
    --card-light: #ffffff;
    --brand-blue: #1a6fb3;
    --sky-blue: #6bbde6;
    --muted: #9fb8cc;
    --white: #ffffff;
  }
  * { box-sizing: border-box; margin: 0; padding: 0; }
  html, body {
    width: 1200px; height: 900px; overflow: hidden;
    background: var(--stage);
    font-family: "Questrial", "Century Gothic", sans-serif;
  }
  .canvas { position: relative; width: 1200px; height: 900px; }
  .card {
    position: absolute; top: 301px; width: 515px; height: 297px;
    box-shadow: 0 6px 14px rgba(0,0,0,0.45);
  }
  .card-front { left: 71px; background: var(--card-dark); }
  .card-back { left: 615px; background: var(--card-light); }

  .front-brand {
    position: absolute; inset: 0;
    display: flex; align-items: center; justify-content: center; gap: 12px;
  }
  .brand-mark { width: 18px; height: 18px; background: var(--sky-blue); }
  .brand-name { color: var(--white); font-size: 30px; letter-spacing: 1px; }

  .back-brand {
    position: absolute; left: 36px; top: 60px;
    display: flex; align-items: center; gap: 9px;
  }
  .back-brand .brand-mark { width: 13px; height: 13px; }
  .back-brand .brand-name { color: var(--brand-blue); font-size: 21px; letter-spacing: 0.5px; }

  .tagline {
    position: absolute; right: 28px; top: 41px;
    text-align: right; color: var(--brand-blue);
    font-size: 12.5px; line-height: 15px;
  }
  .holder { position: absolute; left: 34px; top: 170px; }
  .holder-name { color: var(--brand-blue); font-size: 20px; }
  .holder-license { color: var(--muted); font-size: 11px; margin-top: 5px; }

  .contact-list { position: absolute; left: 34px; top: 225px; list-style: none; }
  .contact-list li {
    display: flex; align-items: center; gap: 9px;
    color: var(--brand-blue); font-size: 16px; line-height: 20px;
  }
  .contact-list svg { width: 12px; height: 12px; fill: var(--sky-blue); flex: none; }
</style>
</head>
<body>
<main class="canvas">
  <section class="card card-front" aria-label="Card front">
    <div class="front-brand">
      <span class="brand-mark"></span>
      <span class="brand-name">Gablestone Inspections</span>
    </div>
  </section>

  <section class="card card-back" aria-label="Card back">
    <div class="back-brand">
      <span class="brand-mark"></span>
      <span class="brand-name">Gablestone Inspections</span>
    </div>
    <p class="tagline">The Intelligent Choice<br>For Home Inspections</p>

    <div class="holder">
      <p class="holder-name">Tobias R. Fenwick</p>
      <p class="holder-license">NY HI License # 27300592415</p>
    </div>

    <ul class="contact-list">
      <li>
        <svg viewBox="0 0 12 12" aria-hidden="true"><path d="M1 5c0-2 2-3.5 5-3.5S11 3 11 5l-2.5.8-.6-1.4H4.1l-.6 1.4zM3 7h6l1 3.5H2z"/></svg>
        555-317-6420
      </li>
      <li>
        <svg viewBox="0 0 12 12" aria-hidden="true"><path d="M0 2.5h12v.8L6 7 0 3.3zM0 4.5l6 3.7 6-3.7V10H0z"/></svg>
        tfenwick@gablestoneinspections.com
      </li>
      <li>
        <svg viewBox="0 0 12 12" aria-hidden="true"><path d="M6 0a6 6 0 1 0 0 12A6 6 0 0 0 6 0zm0 1.2c.7.6 1.2 1.8 1.4 3.2H4.6C4.8 3 5.3 1.8 6 1.2zM1.3 5.4h2.3v1.2H1.3zm3.3 0h2.8v1.2H4.6zm3.8 0h2.3v1.2H8.4zM4.6 7.6h2.8C7.2 9 6.7 10.2 6 10.8 5.3 10.2 4.8 9 4.6 7.6z"/></svg>
        www.gablestoneinspections.com
      </li>
    </ul>
  </section>
</main>
</body>
</html>
```